Business Card

We need a business card for a fundraising/sales and marketing company called Brightwell Giving services. The logo colours are Red Black and white. The final design should communicate professional, reliable yet fun and charity minded
Updates

Sorry for the delay. A decision will be made in the next 48 hours. we are stuck between two designs. Kind Regards, Laura Dunmore

Industry/Entity Type

Marketing

```html
<!DOCTYPE html>
<html lang="en">
<head>
<meta charset="utf-8">
<title>Brightwell Giving services – Business Card</title>
<link rel="stylesheet" href="https://fonts.googleapis.com/css2?family=Arimo:wght@400;700&display=swap">
<style>
  :root {
    --backdrop: #e9e6e2;
    --card: #ffffff;
    --brand-red: #e0141e;
    --ink: #3a3a3a;
    --ink-soft: #555555;
    --band-text: #ffffff;
  }
  * { margin: 0; padding: 0; box-sizing: border-box; }
  html, body {
    width: 1200px; height: 721px; overflow: hidden;
    background: var(--backdrop);
    font-family: "Arimo", Arial, sans-serif;
  }
  .canvas {
    width: 1200px; height: 721px;
    display: flex; align-items: center; justify-content: center;
  }
  .business-card {
    position: relative;
    width: 980px; height: 560px;
    background: var(--card);
    box-shadow: 0 10px 30px rgba(0,0,0,.15);
    overflow: hidden;
  }
  .corner-tab {
    position: absolute; top: 0; right: 0;
    width: 18px; height: 150px;
    background: var(--brand-red);
  }
  .brand {
    position: absolute; left: 150px; top: 250px;
    display: flex; align-items: center; gap: 18px;
  }
  .brand-square {
    width: 34px; height: 34px; background: var(--brand-red);
  }
  .brand-name {
    font-size: 50px; font-weight: 400; letter-spacing: 1px;
    color: var(--ink);
  }
  .contact {
    position: absolute; left: 600px; top: 60px;
    color: var(--ink);
  }
  .contact-name {
    font-size: 32px; font-weight: 400; letter-spacing: .5px;
    line-height: 1;
  }
  .contact-role {
    font-size: 17px; color: var(--brand-red);
    margin: 4px 0 14px;
  }
  .contact-list { list-style: none; }
  .contact-item {
    display: flex; align-items: center; gap: 10px;
    font-size: 17px; color: var(--ink-soft);
    line-height: 25px;
  }
  .contact-icon { width: 16px; height: 16px; fill: var(--brand-red); flex: none; }
  .footer-band {
    position: absolute; left: 0; right: 0; bottom: 0;
    height: 122px; background: var(--brand-red);
    display: flex; align-items: center; justify-content: flex-end;
    padding-right: 70px;
  }
  .website {
    color: var(--band-text); font-size: 22px; letter-spacing: 3px;
  }
</style>
</head>
<body>
<main class="canvas">
  <article class="business-card">
    <div class="corner-tab"></div>

    <div class="brand">
      <span class="brand-square"></span>
      <span class="brand-name">Brightwell Giving</span>
    </div>

    <section class="contact">
      <h1 class="contact-name">YOUR NAME</h1>
      <p class="contact-role">President</p>
      <ul class="contact-list">
        <li class="contact-item">
          <svg class="contact-icon" viewBox="0 0 16 16"><path d="M8 1 1 7h2v8h4v-5h2v5h4V7h2z"/></svg>
          Street No. 23 Harbour
        </li>
        <li class="contact-item">
          <svg class="contact-icon" viewBox="0 0 16 16"><rect x="3" y="1" width="10" height="14" rx="1.5"/></svg>
          + 123.456.789
        </li>
        <li class="contact-item">
          <svg class="contact-icon" viewBox="0 0 16 16"><rect x="1" y="4" width="14" height="10" rx="1"/><rect x="4" y="1" width="8" height="4"/></svg>
          + 123.456.789
        </li>
        <li class="contact-item">
          <svg class="contact-icon" viewBox="0 0 16 16"><path d="M4 1 1 3c0 6 6 12 12 12l2-3-3-3-2 2C8 10 6 8 5 6l2-2z"/></svg>
          + 123.456.789
        </li>
        <li class="contact-item">
          <svg class="contact-icon" viewBox="0 0 16 16"><path d="M1 3h14v10H1z M1 3l7 6 7-6" stroke="#fff" stroke-width="1"/></svg>
          info@brightwellgiving.com
        </li>
      </ul>
    </section>

    <footer class="footer-band">
      <span class="website">www.brightwellgiving.com</span>
    </footer>
  </article>
</main>
</body>
</html>
```